Larkspur Business Card Design

Looking for elegant and super stylish business cards. Enclosed is the card design we are using now. We need something more contemporary.

Target Market(s)

We are a catering company focusing on weddings and corporate events.

Industry/Entity Type

Caterer

Contact Information for Business Card

Please use similar font to our current cards

Colors
0592cd

Requirements
Must have
• Color and be very unique. Also, please use logo (with or without the castle.)

```html
<!DOCTYPE html>
<html lang="en">
<head>
<meta charset="utf-8">
<title>Larkspur Catering &amp; Event Design — Business Card</title>
<link rel="stylesheet" href="https://fonts.googleapis.com/css2?family=Work+Sans:wght@400;500;600&display=swap">
<style>
  :root {
    --brand-blue: #0592cd;
    --ink: #111111;
    --paper: #ffffff;
    --stage: #2a2a2a;
    --text-font: "Work Sans", sans-serif;
  }
  * { margin: 0; padding: 0; box-sizing: border-box; }
  html, body {
    width: 1200px; height: 930px; overflow: hidden;
    background: var(--stage);
    font-family: var(--text-font);
  }
  .card {
    position: absolute;
    width: 680px; height: 390px;
    left: 260px;
  }
  /* Front (blue) */
  .card--front {
    top: 45px;
    background: var(--brand-blue);
    color: var(--paper);
  }
  .wordmark {
    position: absolute;
    display: flex; align-items: center; gap: 22px;
  }
  .wordmark__square {
    width: 110px; height: 110px; flex: none;
  }
  .wordmark__name {
    font-size: 44px; font-weight: 400; letter-spacing: 1px;
    text-transform: uppercase; line-height: 1;
  }
  .wordmark__sub {
    font-size: 17px; font-weight: 400; letter-spacing: 9px;
    text-transform: uppercase; line-height: 1.35; margin-top: 8px;
  }
  .card--front .wordmark { left: 120px; top: 105px; }
  .card--front .wordmark__square { background: var(--paper); }
  .tagline {
    position: absolute; left: 0; right: 0; top: 285px;
    text-align: center; font-size: 17px; line-height: 1.45; letter-spacing: 0.3px;
  }
  /* Back (white) */
  .card--back {
    top: 495px;
    background: var(--paper);
    color: var(--ink);
  }
  .card--back .wordmark { left: 48px; top: 42px; gap: 16px; }
  .card--back .wordmark__square { width: 80px; height: 80px; background: var(--ink); }
  .card--back .wordmark__name { font-size: 32px; }
  .card--back .wordmark__sub { font-size: 13px; letter-spacing: 7px; margin-top: 6px; }
  .person {
    position: absolute; right: 48px; top: 140px; text-align: right;
  }
  .person__name {
    color: var(--brand-blue); font-size: 26px; font-weight: 600;
    text-transform: uppercase; letter-spacing: 1px; line-height: 1.1;
  }
  .person__title { font-size: 16px; margin-top: 2px; }
  .divider {
    position: absolute; left: 48px; right: 48px; top: 200px;
    height: 2px; background: var(--brand-blue);
  }
  .contact-list {
    position: absolute; left: 48px; top: 230px; list-style: none;
    font-size: 17px; line-height: 1.5;
  }
  .contact-list li { display: flex; align-items: center; gap: 12px; }
  .contact-list svg { width: 15px; height: 15px; flex: none; }
  .accent { color: var(--brand-blue); }
  .address {
    position: absolute; right: 48px; top: 230px; text-align: right;
    font-size: 17px; line-height: 1.5; font-style: normal;
  }
</style>
</head>
<body>

<section class="card card--front">
  <div class="wordmark">
    <div class="wordmark__square"></div>
    <div>
      <div class="wordmark__name">The Larkspur</div>
      <div class="wordmark__sub">Catering &amp;<br>Event Design</div>
    </div>
  </div>
  <p class="tagline">Catering - Event Design<br>All-inclusive Packages - Gourmet Events. Skinny Prices.</p>
</section>

<section class="card card--back">
  <div class="wordmark">
    <div class="wordmark__square"></div>
    <div>
      <div class="wordmark__name">The Larkspur</div>
      <div class="wordmark__sub">Catering &amp;<br>Event Design</div>
    </div>
  </div>

  <div class="person">
    <div class="person__name">Marek Halloway</div>
    <div class="person__title">Chief Executive Officer</div>
  </div>

  <div class="divider"></div>

  <ul class="contact-list">
    <li>
      <svg viewBox="0 0 16 16" aria-hidden="true"><path fill="#0592cd" d="M3 1l3 3-1.5 2a9 9 0 0 0 5.5 5.5L12 10l3 3-2 2C6 15 1 10 1 3z"/></svg>
      555 310 4482 ext. 214
    </li>
    <li>
      <svg viewBox="0 0 16 16" aria-hidden="true"><rect x="4" y="1" width="8" height="14" rx="1.5" fill="#0592cd"/><rect x="5.5" y="3" width="5" height="8" fill="#fff"/></svg>
      555 742 0193
    </li>
    <li>
      <svg viewBox="0 0 16 16" aria-hidden="true"><rect x="1.5" y="3.5" width="13" height="9" fill="none" stroke="#0592cd" stroke-width="1.5"/><path d="M1.5 3.5L8 9l6.5-5.5" fill="none" stroke="#0592cd" stroke-width="1.5"/></svg>
      m@thelarkspurcatering.com
    </li>
    <li>
      <svg viewBox="0 0 16 16" aria-hidden="true"><circle cx="8" cy="8" r="6.5" fill="none" stroke="#0592cd" stroke-width="1.3"/><ellipse cx="8" cy="8" rx="2.8" ry="6.5" fill="none" stroke="#0592cd" stroke-width="1.1"/><path d="M1.5 8h13M2.5 5h11M2.5 11h11" stroke="#0592cd" stroke-width="1"/></svg>
      <span>www.<span class="accent">thelarkspurcatering</span>.com</span>
    </li>
  </ul>

  <address class="address">4120 Orchard Lane<br>Mesa Vista, California 90410</address>
</section>

</body>
</html>
```